LumaVantix
stationery - business cards
LumaVantix -
Creative Brief
Professional
Carl MORVEDO
41 Pellin Lane, suite 218 Alderbrook, Oregon, 97310
cm@lumavantix.com
www.lumavantix.com
Free to be creative

```html
<!DOCTYPE html>
<html lang="en">
<head>
<meta charset="utf-8">
<title>LumaVantix Stationery</title>
<link rel="stylesheet" href="https://fonts.googleapis.com/css2?family=Open+Sans:wght@400;600&display=swap">
<style>
  :root {
    --backdrop: #d9dadc;
    --paper: #ffffff;
    --brand-blue: #1f4fa8;
    --brand-blue-deep: #123a86;
    --brand-blue-light: #3f6fc4;
    --ink-grey: #6b6f76;
    --rule-grey: #9a9ea4;
    --rule-dark: #55585d;
    --url-ink: #e8eefa;
  }
  * { box-sizing: border-box; margin: 0; padding: 0; }
  html, body { width: 1200px; height: 915px; overflow: hidden; }
  body {
    background: var(--backdrop);
    font-family: "Open Sans", Arial, sans-serif;
    position: relative;
  }
  .sheet { position: absolute; background: var(--paper); box-shadow: 0 4px 14px rgba(0,0,0,.25); }

  .brand { display: flex; align-items: center; gap: 8px; }
  .brand-square { background: var(--ink-grey); }
  .brand-name { color: var(--ink-grey); font-weight: 400; letter-spacing: .5px; }

  .address { color: var(--ink-grey); line-height: 1.35; }
  .address b { color: var(--brand-blue); font-weight: 600; }

  /* Letterhead */
  .letterhead { left: 111px; top: 104px; width: 545px; height: 712px; overflow: hidden; }
  .letterhead-edge {
    position: absolute; left: 0; top: 0; width: 10px; height: 100%;
    background: linear-gradient(180deg, var(--brand-blue-light), var(--brand-blue-deep) 45%, var(--rule-grey) 70%, var(--rule-dark));
  }
  .letterhead .brand { position: absolute; left: 32px; top: 34px; }
  .letterhead .brand-square { width: 34px; height: 34px; }
  .letterhead .brand-name { font-size: 30px; }
  .letterhead .address { position: absolute; left: 32px; top: 84px; font-size: 10px; }

  /* Business cards */
  .card { width: 228px; height: 124px; }
  .card-front { left: 688px; top: 111px; }
  .card-front .brand { position: absolute; left: 14px; top: 16px; }
  .card-front .brand-square { width: 15px; height: 15px; }
  .card-front .brand-name { font-size: 14px; }
  .card-holder { position: absolute; left: 62px; top: 46px; color: var(--brand-blue); font-size: 9px; font-weight: 600; }
  .card-front .address { position: absolute; left: 62px; top: 66px; font-size: 5.5px; }
  .card-back {
    left: 688px; top: 260px;
    background: radial-gradient(ellipse at 50% 50%, var(--brand-blue-light), var(--brand-blue-deep) 80%);
    display: flex; align-items: center; justify-content: center;
  }
  .card-back-url { color: var(--url-ink); font-size: 9px; letter-spacing: 1.5px; }

  /* Envelope */
  .envelope { left: 485px; top: 420px; width: 621px; height: 342px; overflow: hidden; }
  .envelope-flap {
    position: absolute; left: 0; top: 0; width: 100%; height: 92px;
    background: linear-gradient(180deg, var(--brand-blue-deep), var(--brand-blue) 60%, var(--brand-blue-light));
    display: flex; align-items: center; justify-content: center;
  }
  .envelope-flap-url { color: var(--url-ink); font-size: 9px; letter-spacing: 1.5px; transform: rotate(180deg); }
  .envelope-edge {
    position: absolute; left: 0; top: 92px; width: 8px; height: 250px;
    background: linear-gradient(180deg, var(--rule-grey), var(--rule-dark));
  }
  .envelope .brand { position: absolute; left: 22px; top: 112px; }
  .envelope .brand-square { width: 30px; height: 30px; }
  .envelope .brand-name { font-size: 26px; }
  .envelope .address { position: absolute; left: 22px; top: 150px; font-size: 9px; }
</style>
</head>
<body>
  <section class="sheet letterhead">
    <div class="letterhead-edge"></div>
    <div class="brand"><span class="brand-square"></span><span class="brand-name">LumaVantix</span></div>
    <p class="address">41 Pellin Lane, suite 218<br>Alderbrook, Oregon, 97310<br><b>Phone:</b> (503) 555 0142</p>
  </section>

  <section class="sheet card card-front">
    <div class="brand"><span class="brand-square"></span><span class="brand-name">LumaVantix</span></div>
    <p class="card-holder">Carl MORVEDO</p>
    <p class="address">41 Pellin Lane, suite 218<br>Alderbrook, Oregon, 97310<br><b>Phone:</b> (503) 555 0142<br><b>Email:</b> cm@lumavantix.com</p>
  </section>

  <section class="sheet card card-back">
    <p class="card-back-url">www.lumavantix.com</p>
  </section>

  <section class="sheet envelope">
    <div class="envelope-flap"><p class="envelope-flap-url">www.lumavantix.com</p></div>
    <div class="envelope-edge"></div>
    <div class="brand"><span class="brand-square"></span><span class="brand-name">LumaVantix</span></div>
    <p class="address">41 Pellin Lane, suite 218<br>Alderbrook, Oregon, 97310</p>
  </section>
</body>
</html>
```